Stationery Design Project

We need a stationery design for our Norwegian trucking company. We have existed for about 15 years and our 12 drivers uses relatively new vehicles to transport goods around in northern Norway. Long distance routes with fresh fish og food transport is our main operations.

We have already made alogo that's printed on our trucks. The logo and a picture of our trucks is attached. I think the logo i crappy, but since its already in use, changing it is not an option in this round. Still using a better colour scheme in the overall stationery and more interesting fonts is possible (altso in the logo).

Company details:
Name: Vikstrandbil AS
Organisation nr 981 537 608
Post adress: 8613 Lysvær

I like minimalism and simplicity. I am avalibly for questions in normal GMT working hours either here or on mail: petter@vikstrand.no

Reason: Hi. Im extending the deadline because I needed some time to find a vector file of our logo. Sorry for the inconvenience

Hi, and thanks for all your interest in the project. Some updates:

-          I have decided to commit to using one of the designs. Some designer will get the payment.

-          I have extended the deadline with 24 hours since I needed some time to find our firms vector logo (a slow Swedish man was holding me up)

-          We will not choose a design before the deadline. No need to rush.

-          We have received a lot of great design and think there is a need to specified the product we want to make:

o   Business Card for all our employers. I just need the design and will duplicate with the correct numbers and name myself. The information on should be: Logo, employer’s name, Phone number, email, website, Postal number and address. Use this as a template: logo, Leif Brattli, 47283916, Leif@vikstrand.no,, vikstrand.no, 8613 Lysvær. The order and placement of the information is your creative decision.

o   Stickers to put on the goods we travel. On the sticker the should be the following information: Logo, phone number, Tekst and link: Fraktæ av Vikstrandbil. Ke du syns? Vikstrand.no/tilbakemelding (this means: Handled by Vikstrandbil. What do you think Vikstrand.no/feedback -à the link will be a feedback form). The placement the information and size is your creative decision with some stings: we have been thinking of using Prentavo for printing and see that a size about 6x6 cm, 8x5 or something like that. (with 3000 copies our budget is 200 punds). Any suggestions of other suppliers are welcome. Prentavo price calculator http://www.prentavoprint.co.uk/digital-litho-printing/printing-labels-tags/stickers/

o   Letterhead with logo, address, phone number and organizational number.

o   Envelopes with logo,address, phone number and organizational number.

Have a nice day.

 

 

• Using the blue colour in the logo and using a similar graphic approch.

```html
<!DOCTYPE html>
<html lang="no">
<head>
<meta charset="utf-8">
<title>Vikstrandbil – klistremerke</title>
<link href="https://fonts.googleapis.com/css2?family=Play:wght@400;700&display=swap" rel="stylesheet">
<style>
  :root {
    --page-bg: #eceeee;
    --sticker-white: #ffffff;
    --navy: #0b2f86;
    --sky: #1b77d1;
    --ink: #2b2b2b;
    --white: #ffffff;
  }
  html, body {
    margin: 0;
    padding: 0;
    width: 1200px;
    height: 900px;
    overflow: hidden;
    background: var(--page-bg);
  }
  .sticker {
    display: block;
    width: 1200px;
    height: 900px;
    font-family: "Play", sans-serif;
  }
  .sticker__face { fill: var(--sticker-white); }
  .sticker__rim { fill: none; stroke: var(--navy); stroke-width: 12; }
  .brand__mark { fill: var(--navy); }
  .brand__name { fill: var(--navy); font-size: 56px; font-weight: 700; }
  .message__line { fill: var(--ink); font-size: 33px; }
  .message__question { fill: var(--ink); font-size: 40px; }
  .link-band { fill: var(--navy); }
  .link-band__text { fill: var(--white); font-size: 37px; }
  .phone-band { fill: var(--sky); }
  .phone-band__icon { fill: none; stroke: var(--white); stroke-width: 2; }
  .phone-band__icon-dot { fill: var(--white); }
  .phone-band__text { fill: var(--white); font-size: 29px; letter-spacing: 1px; }
</style>
</head>
<body>
<svg class="sticker" viewBox="0 0 1200 900" xmlns="http://www.w3.org/2000/svg" aria-label="Vikstrandbil klistremerke">
  <defs>
    <clipPath id="sticker-inner">
      <circle cx="600" cy="450" r="289"/>
    </clipPath>
  </defs>

  <circle class="sticker__face" cx="600" cy="450" r="295"/>

  <g class="brand">
    <circle class="brand__mark" cx="392" cy="322" r="14"/>
    <text class="brand__name" x="420" y="342">Vikstrandbil</text>
  </g>

  <g class="message" text-anchor="middle">
    <text class="message__line" x="593" y="456">Fraktæ av Vikstrandbil.</text>
    <text class="message__question" x="593" y="507">KE DU SYNS?</text>
  </g>

  <g clip-path="url(#sticker-inner)">
    <polygon class="link-band" points="300,521 860,521 832,567 300,567"/>
    <text class="link-band__text" x="592" y="556" text-anchor="middle">Vikstrand.no/tilbakemelding</text>

    <polygon class="phone-band" points="490,632 820,632 800,668 467,668"/>
    <g class="phone-band__icon">
      <rect x="509" y="639" width="9" height="22" rx="2"/>
      <rect x="518" y="642" width="12" height="19" rx="1"/>
    </g>
    <g class="phone-band__icon-dot">
      <rect x="521" y="645" width="6" height="3"/>
      <rect x="521" y="651" width="2" height="2"/><rect x="525" y="651" width="2" height="2"/>
      <rect x="521" y="655" width="2" height="2"/><rect x="525" y="655" width="2" height="2"/>
    </g>
    <text class="phone-band__text" x="555" y="661">981 537 608</text>
  </g>

  <circle class="sticker__rim" cx="600" cy="450" r="289"/>
</svg>
</body>
</html>
```